Tarrow Creek plumbing plumbing company business card design

Something sinilar to business card i upload it is my old business card design
And have a good watermark with the logo or majority of the logot in rhe background as watermark

Plumbing business similar to uploaded design with a nice watermark of the logo

Font styles to use
Script

Colors

Designer to choose colors to be used in the design.

```html
<!DOCTYPE html>
<html lang="en">
<head>
<meta charset="utf-8">
<title>Tarrow Creek Plumbing – Business Card</title>
<link href="https://fonts.googleapis.com/css2?family=Dancing+Script:wght@700&family=Montserrat:wght@600;700&family=Roboto:wght@400;500;700&display=swap" rel="stylesheet">
<style>
  :root {
    --bg: #2b2b2b;
    --blue: #0b56a8;
    --blue-deep: #074a92;
    --emboss: #0c3d78;
    --accent: #1a66b3;
    --card-dark: #161616;
    --text-light: #dedede;
    --white: #ececec;
  }
  * { margin: 0; padding: 0; box-sizing: border-box; }
  html, body { width: 1200px; height: 1138px; overflow: hidden; background: var(--bg); }
  .canvas { position: relative; width: 1200px; height: 1138px; }

  .card { position: absolute; border-radius: 14px; overflow: hidden; }

  .card-front {
    left: 274px; top: 186px; width: 623px; height: 375px;
    background: linear-gradient(180deg, var(--blue) 0%, var(--blue-deep) 100%);
    display: flex; align-items: center; justify-content: center;
  }
  .front-watermark {
    font-family: "Dancing Script", cursive; font-weight: 700;
    color: var(--emboss); text-align: center;
    font-size: 76px; line-height: 1.05;
  }

  .card-back {
    left: 276px; top: 608px; width: 618px; height: 373px;
    background: var(--card-dark);
  }
  .back-name {
    position: absolute; left: 31px; top: 48px;
    font-family: "Montserrat", sans-serif; font-weight: 700;
    color: var(--white); text-transform: uppercase;
    font-size: 30px; line-height: 1.1; letter-spacing: 1px;
  }
  .side-tab {
    position: absolute; left: -76px; top: 162px; width: 90px; height: 90px;
    border-radius: 50%; background: var(--accent);
  }
  .person-name {
    position: absolute; left: 31px; top: 168px;
    font-family: "Roboto", sans-serif; font-weight: 700;
    color: var(--accent); font-size: 26px; line-height: 32px;
  }
  .person-role {
    position: absolute; left: 31px; top: 203px;
    font-family: "Roboto", sans-serif; font-weight: 400;
    color: var(--text-light); font-size: 16px; line-height: 20px;
  }
  .contact-list { position: absolute; left: 31px; top: 250px; list-style: none; }
  .contact-list li {
    display: flex; align-items: center; gap: 12px; height: 24px;
    font-family: "Roboto", sans-serif; font-size: 16px; color: var(--text-light);
  }
  .contact-list svg { width: 15px; height: 15px; fill: var(--accent); flex: none; }
  .address {
    position: absolute; left: 31px; top: 329px;
    font-family: "Roboto", sans-serif; font-size: 16px; line-height: 20px; color: var(--text-light);
  }
  .tap-art {
    position: absolute; left: 326px; top: 64px; width: 292px; height: 218px;
    background: linear-gradient(135deg, rgba(26,102,179,0.35) 0%, rgba(26,102,179,0.9) 100%);
    border-radius: 10px 0 0 10px;
  }
</style>
</head>
<body>
<div class="canvas">

  <section class="card card-front">
    <div class="front-watermark">Tarrow Creek<br>Plumbing</div>
  </section>

  <section class="card card-back">
    <div class="back-name">Tarrow Creek<br>Plumbing</div>
    <div class="tap-art" role="img" aria-label="Large water tap illustration in blue"></div>
    <div class="side-tab"></div>

    <div class="person-name">DANA MERCER</div>
    <div class="person-role">Managing Principal</div>

    <ul class="contact-list">
      <li>
        <svg viewBox="0 0 16 16"><path d="M3 6c0-2 2-3 5-3s5 1 5 3l-2 1-1-1.5H6L5 7zM4 8h8l1 5H3z"/></svg>
        555-0142-7788
      </li>
      <li>
        <svg viewBox="0 0 16 16"><path d="M1 4h14v9H1z M1 4l7 5 7-5" stroke="#161616" stroke-width="1"/></svg>
        dana@tarrowcreekplumbing.com
      </li>
      <li>
        <svg viewBox="0 0 16 16"><circle cx="8" cy="8" r="6.5"/><path d="M1.5 8h13M8 1.5v13M3 4.5h10M3 11.5h10" stroke="#161616" stroke-width="1" fill="none"/></svg>
        www.tarrowcreekplumbing.com
      </li>
    </ul>

    <div class="address">18 Ridge Lane, Any City, Any Town, Tarrow 204519</div>
  </section>

</div>
</body>
</html>
```